Culture Blueprint

I would like to edit the design of this culture blueprint graphic to align with my brand colors and services graphic. Please
The KITE stands for Leadership, Engagement, Activate Culture and Distinguish.
Work to be done:
1. Please make Purpose in red brand "kite" color
2. Please make Philosophy in grey brand "engage" color
3. Please make Priorities in and Processes (internal and external) in orange brand "active" color
4. Please make projections in teal "distinguish" color

Creativity welcomed!

```html
<!DOCTYPE html>
<html lang="en">
<head>
<meta charset="utf-8">
<title>Culture Blueprint</title>
<link rel="stylesheet" href="https://fonts.googleapis.com/css2?family=Crimson+Text:ital,wght@0,400;0,600;0,700;1,400&display=swap">
<style>
  :root {
    --page: #ffffff;
    --distinguish: #14808a;
    --distinguish-ink: #ffffff;
    --active-outer: #ef7d22;
    --active-mid: #f59a47;
    --active-inner: #e8671a;
    --active-ink: #2b1406;
    --engage: #5e6166;
    --engage-ink: #ffffff;
    --kite: #d2232a;
    --kite-ink: #ffffff;
    --divider: #ffffff;
    --flow: rgba(255, 255, 255, 0.85);
  }
  html, body {
    margin: 0;
    padding: 0;
    width: 1200px;
    height: 1074px;
    overflow: hidden;
    background: var(--page);
  }
  .blueprint {
    display: block;
    width: 1200px;
    height: 1074px;
    font-family: "Crimson Text", Georgia, serif;
  }
  .label { text-anchor: middle; dominant-baseline: middle; }
  .label--projection { font-size: 15px; font-style: italic; fill: var(--distinguish-ink); }
  .label--external { font-size: 16px; fill: var(--active-ink); }
  .label--internal { font-size: 15px; fill: var(--active-ink); }
  .label--priorities { font-size: 28px; font-weight: 700; fill: var(--active-ink); }
  .label--philosophy { font-size: 22px; font-weight: 700; fill: var(--engage-ink); }
  .label--purpose { font-size: 22px; font-weight: 600; fill: var(--kite-ink); }
  .divider { stroke: var(--divider); stroke-width: 3; }
  .ring-line { fill: none; stroke: var(--divider); stroke-width: 3; }
  .flow { stroke: var(--flow); stroke-width: 3; fill: none; }
</style>
</head>
<body>
<svg class="blueprint" viewBox="0 0 850 761" xmlns="http://www.w3.org/2000/svg" role="img" aria-label="Culture blueprint: Purpose, Philosophy, Priorities, Processes and Projections">
  <defs>
    <marker id="flow-head" viewBox="0 0 10 10" refX="8" refY="5" markerWidth="5" markerHeight="5" orient="auto">
      <path d="M0 0 L10 5 L0 10 Z" fill="var(--flow)"/>
    </marker>
    <path id="arc-priorities" d="M -124 0 A 124 124 0 0 1 124 0"/>
    <path id="arc-philosophy" d="M -76 0 A 76 76 0 0 1 76 0"/>
  </defs>

  <g class="wheel" transform="translate(425 380)">
    <!-- Projections -->
    <circle class="ring ring--projections" r="340" fill="var(--distinguish)"/>
    <g class="dividers-projection">
      <line class="divider" x1="0" y1="-270" x2="0" y2="-340" transform="rotate(21)"/>
      <line class="divider" x1="0" y1="-270" x2="0" y2="-340" transform="rotate(66)"/>
      <line class="divider" x1="0" y1="-270" x2="0" y2="-340" transform="rotate(112)"/>
      <line class="divider" x1="0" y1="-270" x2="0" y2="-340" transform="rotate(157)"/>
      <line class="divider" x1="0" y1="-270" x2="0" y2="-340" transform="rotate(203)"/>
      <line class="divider" x1="0" y1="-270" x2="0" y2="-340" transform="rotate(248)"/>
      <line class="divider" x1="0" y1="-270" x2="0" y2="-340" transform="rotate(294)"/>
      <line class="divider" x1="0" y1="-270" x2="0" y2="-340" transform="rotate(339)"/>
    </g>

    <!-- External processes -->
    <circle class="ring ring--external" r="270" fill="var(--active-outer)"/>
    <circle class="ring-line" r="270"/>
    <g class="dividers-external">
      <line class="divider" x1="0" y1="-210" x2="0" y2="-270" transform="rotate(32)"/>
      <line class="divider" x1="0" y1="-210" x2="0" y2="-270" transform="rotate(102)"/>
      <line class="divider" x1="0" y1="-210" x2="0" y2="-270" transform="rotate(180)"/>
      <line class="divider" x1="0" y1="-210" x2="0" y2="-270" transform="rotate(256)"/>
      <line class="divider" x1="0" y1="-210" x2="0" y2="-270" transform="rotate(328)"/>
    </g>

    <!-- Internal processes -->
    <circle class="ring ring--internal" r="210" fill="var(--active-mid)"/>
    <circle class="ring-line" r="210"/>
    <g class="dividers-internal">
      <line class="divider" x1="0" y1="-150" x2="0" y2="-210" transform="rotate(30)"/>
      <line class="divider" x1="0" y1="-150" x2="0" y2="-210" transform="rotate(90)"/>
      <line class="divider" x1="0" y1="-150" x2="0" y2="-210" transform="rotate(150)"/>
      <line class="divider" x1="0" y1="-150" x2="0" y2="-210" transform="rotate(210)"/>
      <line class="divider" x1="0" y1="-150" x2="0" y2="-210" transform="rotate(270)"/>
      <line class="divider" x1="0" y1="-150" x2="0" y2="-210" transform="rotate(330)"/>
    </g>

    <!-- Priorities -->
    <circle class="ring ring--priorities" r="150" fill="var(--active-inner)"/>
    <circle class="ring-line" r="150"/>

    <!-- Flows from the core into each process -->
    <g class="flows">
      <line class="flow" x1="0" y1="-106" x2="0" y2="-144" marker-end="url(#flow-head)" transform="rotate(60)"/>
      <line class="flow" x1="0" y1="-106" x2="0" y2="-144" marker-end="url(#flow-head)" transform="rotate(120)"/>
      <line class="flow" x1="0" y1="-106" x2="0" y2="-144" marker-end="url(#flow-head)" transform="rotate(180)"/>
      <line class="flow" x1="0" y1="-106" x2="0" y2="-144" marker-end="url(#flow-head)" transform="rotate(240)"/>
      <line class="flow" x1="0" y1="-106" x2="0" y2="-144" marker-end="url(#flow-head)" transform="rotate(300)"/>
    </g>

    <!-- Philosophy & Purpose -->
    <circle class="ring ring--philosophy" r="100" fill="var(--engage)"/>
    <circle class="ring-line" r="100"/>
    <circle class="core core--purpose" r="48" fill="var(--kite)"/>
    <circle class="ring-line" r="48"/>

    <text class="label label--priorities"><textPath href="#arc-priorities" startOffset="50%">Priorities</textPath></text>
    <text class="label label--philosophy"><textPath href="#arc-philosophy" startOffset="50%">Philosophy</textPath></text>
    <text class="label label--purpose" y="1">Purpose</text>

    <!-- Projection labels -->
    <g class="labels-projection">
      <text class="label label--projection" transform="rotate(0) translate(0 -306)">Name</text>
      <text class="label label--projection" transform="rotate(43.5) translate(0 -306)">Logo / Symbols</text>
      <text class="label label--projection" transform="rotate(89) translate(0 -306)">Headquarters</text>
      <text class="label label--projection" transform="rotate(-45.5) translate(0 306)">Leader Image</text>
      <text class="label label--projection" transform="rotate(0) translate(0 306)">Offices / Stores</text>
      <text class="label label--projection" transform="rotate(45.5) translate(0 306)">Dress / Uniforms</text>
      <text class="label label--projection" transform="rotate(-89) translate(0 -306)">Marketing/PR/Advertising</text>
      <text class="label label--projection" transform="rotate(-43.5) translate(0 -306)">Community Activities</text>
    </g>

    <!-- External process labels -->
    <g class="labels-external">
      <text class="label label--external" transform="rotate(0) translate(0 -240)">Customers</text>
      <text class="label label--external" transform="rotate(67) translate(0 -240)">Markets</text>
      <text class="label label--external" transform="rotate(-39) translate(0 240)">Products</text>
      <text class="label label--external" transform="rotate(38) translate(0 240)">Services</text>
      <text class="label label--external" transform="rotate(-68) translate(0 -240)">Suppliers / Vendors &amp; Partners</text>
    </g>

    <!-- Internal process labels -->
    <g class="labels-internal">
      <text class="label label--internal" transform="rotate(0) translate(0 -180)"><tspan x="0" dy="-8">Structure, Work</tspan><tspan x="0" dy="17">Design &amp; Systems</tspan></text>
      <text class="label label--internal" transform="rotate(60) translate(0 -180)"><tspan x="0" dy="-8">Recruitment</tspan><tspan x="0" dy="17">&amp; Selection</tspan></text>
      <text class="label label--internal" transform="rotate(-60) translate(0 180)"><tspan x="0" dy="-8">Training &amp;</tspan><tspan x="0" dy="17">Development</tspan></text>
      <text class="label label--internal" transform="rotate(0) translate(0 180)"><tspan x="0" dy="-8">Performance</tspan><tspan x="0" dy="17">Management</tspan></text>
      <text class="label label--internal" transform="rotate(60) translate(0 180)"><tspan x="0" dy="-8">Internal</tspan><tspan x="0" dy="17">Communications</tspan></text>
      <text class="label label--internal" transform="rotate(-60) translate(0 -180)">Technology</text>
    </g>
  </g>
</svg>
</body>
</html>
```